The Brightwater Compass Business Card

We need an attractive business card with the logo that we bought from ArtVantly last year.
Our mission is to contribute to change the way today's leaders manage business companies bringing value to the workplace and helping them to build a new model of creating wealth.
Our logo is clear about our values : we seek Positive Change through People and are convinced that the pursuit of individual well-being and the chase of economic results can converge with the right management.
Management Consulting
Corinne Fabrelle
+34 612 98 70 31
corinne.fabrelle@thebrightwatercompass-mail.net
www.thebrightwatercompass-mail.net

```html
<!DOCTYPE html>
<html lang="en">
<head>
<meta charset="utf-8">
<title>The Brightwater Compass – Business Card</title>
<link rel="stylesheet" href="https://fonts.googleapis.com/css2?family=Tinos&family=Cinzel:wght@500&family=Open+Sans:wght@400&display=swap">
<style>
  :root {
    --page: #ffffff;
    --front-bg: #33b8a2;
    --back-bg: #cfe8e4;
    --title-band: #a6ddd3;
    --ink-dark: #1f3b38;
    --white: #ffffff;
    --brand: #2a8a83;
    --decor: #5cc7b5;
  }
  * { margin: 0; padding: 0; box-sizing: border-box; }
  html, body {
    width: 1200px;
    height: 849px;
    overflow: hidden;
    background: var(--page);
  }
  .canvas {
    position: relative;
    width: 1200px;
    height: 849px;
  }
  .card {
    position: absolute;
    left: 322px;
    width: 548px;
    height: 312px;
    border-radius: 15px;
    overflow: hidden;
  }
  .card--front { top: 109px; background: var(--front-bg); }
  .card--back { top: 456px; background: var(--back-bg); }

  .front__decor {
    position: absolute;
    left: 0;
    top: 0;
    width: 240px;
    height: 250px;
    background: radial-gradient(ellipse at 20% 45%, var(--decor), rgba(92,199,181,0) 70%);
  }
  .front__identity {
    position: absolute;
    right: 44px;
    top: 40px;
    text-align: right;
  }
  .front__name {
    font-family: "Tinos", "Times New Roman", serif;
    font-size: 27px;
    letter-spacing: 0.3px;
    color: var(--white);
    text-transform: uppercase;
    line-height: 1;
  }
  .front__role {
    display: inline-block;
    margin-top: 5px;
    padding: 1px 2px 1px 5px;
    background: var(--title-band);
    font-family: "Open Sans", Arial, sans-serif;
    font-size: 13px;
    letter-spacing: 4.3px;
    color: var(--ink-dark);
    text-transform: uppercase;
    line-height: 15px;
  }
  .contact {
    position: absolute;
    right: 44px;
    list-style: none;
    top: 195px;
  }
  .contact__item {
    display: flex;
    justify-content: flex-end;
    align-items: center;
    gap: 12px;
    height: 35px;
    font-family: "Open Sans", Arial, sans-serif;
    font-size: 14px;
    color: var(--white);
  }
  .contact__icon { width: 18px; height: 18px; flex: none; }

  .back__brand {
    position: absolute;
    left: 0;
    right: 0;
    top: 118px;
    display: flex;
    flex-direction: column;
    align-items: center;
    gap: 14px;
  }
  .back__mark {
    width: 22px;
    height: 22px;
    border-radius: 50%;
    background: var(--brand);
  }
  .back__name {
    font-family: "Cinzel", "Times New Roman", serif;
    font-weight: 500;
    font-size: 29px;
    color: var(--brand);
    line-height: 1;
  }
  .back__web {
    position: absolute;
    left: 0;
    right: 0;
    bottom: 19px;
    text-align: center;
    font-family: "Open Sans", Arial, sans-serif;
    font-size: 14px;
    color: var(--brand);
  }
</style>
</head>
<body>
<main class="canvas">
  <section class="card card--front">
    <div class="front__decor" role="img" aria-label="Decorative brand foliage area"></div>
    <div class="front__identity">
      <h1 class="front__name">Corinne Fabrelle</h1>
      <p class="front__role">Creative Director</p>
    </div>
    <ul class="contact">
      <li class="contact__item">
        <span>+34 612 98 70 31</span>
        <svg class="contact__icon" viewBox="0 0 20 20" aria-hidden="true">
          <path fill="#fff" d="M2 7c0-2 4-3 8-3s8 1 8 3v2h-4V7H6v2H2z"/>
          <path fill="#fff" d="M5 10h10l2 6H3z"/>
          <circle cx="10" cy="13" r="1.8" fill="#33b8a2"/>
        </svg>
      </li>
      <li class="contact__item">
        <span>corinne.fabrelle@thebrightwatercompass-mail.net</span>
        <svg class="contact__icon" viewBox="0 0 20 20" aria-hidden="true">
          <rect x="2" y="5" width="16" height="11" fill="none" stroke="#fff" stroke-width="1.5"/>
          <path d="M2 5l8 6 8-6M2 16l6-5M18 16l-6-5" fill="none" stroke="#fff" stroke-width="1.3"/>
        </svg>
      </li>
      <li class="contact__item">
        <span>www.thebrightwatercompass-mail.net</span>
        <svg class="contact__icon" viewBox="0 0 20 20" aria-hidden="true">
          <g fill="none" stroke="#fff" stroke-width="1.3">
            <circle cx="10" cy="10" r="7.5"/>
            <ellipse cx="10" cy="10" rx="3.3" ry="7.5"/>
            <path d="M2.5 10h15M4 6h12M4 14h12"/>
          </g>
        </svg>
      </li>
    </ul>
  </section>

  <section class="card card--back">
    <div class="back__brand">
      <span class="back__mark" aria-hidden="true"></span>
      <p class="back__name">The Brightwater Compass</p>
    </div>
    <p class="back__web">www.thebrightwatercompass-mail.net</p>
  </section>
</main>
</body>
</html>
```